Elegant, High End Integrated Wellness Healthcare Practice

We need a brochure designed for an integrated mind-body wellness healthcare practice (www.larchveilclinic.com) . This brochure will be used when we cold call prospects (physicians to refer to our office, and potential consumers to utilize our services). Our practice is geographically located in the middle Tennessee USA region, although we have plans to become an international company as many of our offerings can be accessed anywhere in the world. Ultimately our goal is to have this brochure used as a leave-behind in an effort to introduce our integrated offerings to increase market share. The final product brochure should be both elegant and serious, with clean lines but also convey warmth and trust, as individuals who are coming for our services have usually struggled with their health for a significant amount of time before finding our practice.

The design brief was very specific about providing a high-end science-based 2-page brochure (not flier). Several designs submitted were fliers. The other designs were heavy on yoga or "woo woo" non-science-based looking pictures. This is a flier to appeal to physicians and other healthcare providers. Therefore the design must speak science and evidence-based methods of mind and body wellness care. I would also like to appeal to the other designers I paid extra for their submissions and who have indicated they will "respond in the coming days."

```html
<!DOCTYPE html>
<html lang="en">
<head>
<meta charset="utf-8">
<title>Larchveil Clinic – Book a 10 Minute Consultation</title>
<link href="https://fonts.googleapis.com/css2?family=Montserrat:wght@300;400;700;800&display=swap" rel="stylesheet">
<style>
  :root {
    --green-top: #70a841;
    --green-mid: #63ad62;
    --teal: #56b493;
    --teal-soft: #8fd0b8;
    --white: #ffffff;
    --ink: #1d3608;
    --body-ink: #2f4a1a;
    --slate: #2f5561;
    --dot: #3fb39a;
    --brain: #6aa83f;
  }
  * { box-sizing: border-box; margin: 0; padding: 0; }
  html, body { width: 1200px; height: 927px; overflow: hidden; background: var(--white); }
  body { font-family: "Montserrat", sans-serif; }
  .brochure { position: relative; width: 1200px; height: 927px; overflow: hidden; background: var(--white); }

  .cover-panel {
    position: absolute; left: 0; top: 0; width: 560px; height: 927px;
    background: linear-gradient(180deg, var(--green-top) 0%, var(--green-mid) 40%, var(--teal) 60%, var(--teal-soft) 72%, var(--white) 90%);
  }
  .spine-art {
    position: absolute; left: 505px; top: 0; width: 170px; height: 927px;
    background: linear-gradient(180deg, #55b79b 0%, #6aa83b 30%, #43ad0c 60%, #1f8a05 78%, #0b4f22 100%);
    border-radius: 0 0 40px 40px;
  }
  .portrait {
    position: absolute; left: 250px; top: 415px; width: 330px; height: 512px;
    background: linear-gradient(180deg, #e9ddd3 0%, #d8b8a0 35%, #14b3c3 55%, #0fa3b4 100%);
    border-radius: 160px 160px 0 0;
    border: 8px solid var(--white); border-bottom: none;
  }

  .headline {
    position: absolute; left: 52px; top: 88px;
    color: var(--white); font-weight: 800; font-size: 54px; line-height: 46px;
    letter-spacing: 0.5px;
  }
  .lead {
    position: absolute; left: 58px; top: 236px; width: 420px;
    color: var(--white); font-weight: 300; font-size: 26px; line-height: 31.5px;
  }
  .contact-list { position: absolute; left: 74px; top: 364px; list-style: none; color: var(--white); font-weight: 300; font-size: 18px; line-height: 22px; }
  .contact-list li { display: flex; align-items: flex-start; gap: 12px; margin-bottom: 15px; }
  .contact-list svg { width: 24px; height: 24px; flex: none; margin-top: -1px; }
  .copyright { position: absolute; left: 58px; top: 892px; font-size: 8px; color: #4d5a4d; }

  .brand { position: absolute; left: 856px; top: 43px; display: flex; align-items: center; gap: 8px; }
  .brand-mark { width: 44px; height: 44px; border-radius: 50%; background: var(--brain); }
  .brand-name { font-weight: 700; font-size: 17px; line-height: 21px; color: var(--ink); width: 110px; }

  .dots { position: absolute; display: grid; grid-template-columns: repeat(5, 15px); row-gap: 8px; }
  .dots span { width: 5px; height: 5px; border-radius: 50%; background: var(--dot); }
  .dots .offset { margin-left: 8px; }

  .tagline {
    position: absolute; left: 740px; top: 136px; width: 395px; text-align: center;
    font-weight: 700; font-size: 34px; line-height: 39px; color: var(--ink);
  }
  .science-art {
    position: absolute; left: 770px; top: 260px; width: 355px; height: 330px;
    background: radial-gradient(ellipse at 50% 50%, #6aa83f 0%, #8dc06a 38%, #e8f2e0 62%, var(--white) 75%);
  }
  .about {
    position: absolute; left: 730px; top: 628px; width: 415px; text-align: center;
    font-weight: 400; font-size: 18.5px; line-height: 22px; color: var(--body-ink);
  }
  .social { position: absolute; left: 826px; top: 813px; display: flex; align-items: center; gap: 8px; }
  .social span { width: 22px; height: 22px; border-radius: 50%; background: var(--slate); }
  .social p { margin-left: 6px; font-size: 19px; color: var(--slate); font-weight: 400; }
</style>
</head>
<body>
<main class="brochure">
  <div class="cover-panel"></div>
  <div class="spine-art" role="img" aria-label="Illustrated column of green spinal vertebrae"></div>
  <div class="portrait" role="img" aria-label="Photo of a smiling clinician in teal scrubs holding a stethoscope"></div>

  <h1 class="headline">BOOK A<br>10 MINUTE<br>CONSULATION</h1>
  <p class="lead">And find out how a body and mind consultation can help you live your best life.</p>

  <ul class="contact-list">
    <li>
      <svg viewBox="0 0 24 24"><rect x="1" y="4" width="22" height="16" rx="2" fill="#fff"/><path d="M2 6l10 7 10-7" fill="none" stroke="#70a841" stroke-width="1.8"/></svg>
      <span>hello@larchveilclinic.com</span>
    </li>
    <li>
      <svg viewBox="0 0 24 24"><path d="M12 2L1 12h3v10h6v-6h4v6h6V12h3z" fill="#fff"/></svg>
      <span>418 Quillmore Ridge Rd,<br>Ashbend, TN 37190,<br>United States</span>
    </li>
    <li>
      <svg viewBox="0 0 24 24"><circle cx="12" cy="12" r="11" fill="#fff"/><path d="M8.2 6.5l2 2.3-1.1 1.6c.8 1.7 2 2.9 3.6 3.7l1.6-1.1 2.3 2-1.2 1.8c-3.9-.4-7.4-3.9-7.9-7.9z" fill="#56b493"/></svg>
      <span>+1 615-555-0142</span>
    </li>
  </ul>

  <p class="copyright">© 2023 Larchveil Clinic Ltd., All rights reserved.</p>

  <div class="brand">
    <span class="brand-mark"></span>
    <span class="brand-name">LARCHVEIL CLINIC</span>
  </div>

  <div class="dots" style="left:1068px; top:107px;">
    <span></span><span></span><span></span><span></span><span></span>
    <span class="offset"></span><span class="offset"></span><span class="offset"></span><span class="offset"></span><span class="offset"></span>
  </div>

  <h2 class="tagline">Discover A Better Way To A Better You</h2>

  <div class="science-art" role="img" aria-label="Illustration of a green brain with molecule structures and a test tube"></div>

  <p class="about">At Larchveil Clinic we facilitate body and mind health and wellness through an integrated functional approach to care. This method of personalized care appreciates you as a unique individual with distinct health circumstances.</p>

  <div class="social">
    <span></span><span></span><span></span>
    <p>@larchveilclinic</p>
  </div>

  <div class="dots" style="left:700px; top:868px;">
    <span></span><span></span><span></span><span></span><span></span>
    <span class="offset"></span><span class="offset"></span><span class="offset"></span><span class="offset"></span><span class="offset"></span>
  </div>
</main>
</body>
</html>
```